Medical Software Informational Flyer and Website Design

Our company, Copper Vale Systems, is launching a new product, the Copper Vale Clinic Workflow Hub. It is a software suite that will increase the productivity and volume of a LASIK practice.

We want this flyer to be a companion to our big reveal presentation at OLV and PEMWG; it's primary purpose is to inform potential clients on the many ways this software will help their practice. It is also obviously a promotional material. Because it is a companion to our presentation, we feel that it is acceptable for the flyer to contain much more text than would normally be reasonable in a flyer; it will go into more detail about the 12 major selling points of our software than our presentation time will allow. Having said that, however, we still want there to be "breathing room" for the design and the viewer's eyes.

We have uploaded our logo, both in full color and in white with no background (often used for watermarks, but certainly not restricted for that use alone). Our logo should be accompanied by either "Copper Vale Systems" or "Copper Vale" using the Trajan Pro font (unoriginal, we know, but it's what we've chosen). We have included a color palette that compliments our logo, but designs are not limited to that palette (for example, we have found a pink (#cc1448) that compliments the palette and that we have used in the presentation).

We have also uploaded a PSD that includes icons that could compliment 9 of the 12 major selling points for the Copper Vale Clinic Workflow Hub software (the category titles are subject to change). The icons are not necessarily set in stone. For consistency with our presentation, the Protection, Integration, and Review icons should be used, but any of the remaining six (in particular, the Personalized icon) can be changed to whatever you think might be more suitable. The PSD also has some preliminary text for a few of the 12 selling points (we are refining the text now and will get the final content to designers very soon). Also note that the font is simply a placeholder; use whatever font you think would best compliment your design. Finally, keep in mind that the PSD does NOT reflect a design we are looking for; in fact, we hate this "design" and hesitate to call it a design. It was simply a way to arrange the elements to easily distribute them to designers.

We want an 8 1/2in x 11in 8-page flyer that is professional, simple, and has a clear message: this product will revolutionize your practice! We of course also need a website design that compliments the flyer design once the flyer design is finalized and chosen.

We will be monitoring this project closely-- please ask any questions you have!
Updates

Target Market(s)

Physicians, technicians, and marketing personnel in the LASIK industry.

Industry/Entity Type

Software

Number of Pages Required

4 page

Font styles to use
Serif
Sans Serif

```html
<!DOCTYPE html>
<html lang="en">
<head>
<meta charset="utf-8">
<title>Copper Vale Systems – Clinic Workflow Hub</title>
<link href="https://fonts.googleapis.com/css2?family=Cinzel:wght@600&family=Lato:wght@400&display=swap" rel="stylesheet">
<style>
  :root{
    --stage:#e9e6dc;
    --yellow:#f3ec36;
    --green:#bfd840;
    --navy:#0c2a39;
    --teal:#17795f;
    --paper-text:#ffffff;
    --pale:#f7f3a6;
  }
  *{box-sizing:border-box;margin:0;padding:0}
  html,body{width:958px;height:1200px;overflow:hidden;background:var(--stage)}
  .flyer-frame{position:absolute;left:15px;top:0;width:928px;height:1200px;overflow:hidden}
  .flyer{position:absolute;left:0;top:0;width:1048px;height:1356px;transform:scale(.8855);transform-origin:0 0;background:var(--yellow);font-family:"Lato",sans-serif}
  .backdrop{position:absolute;inset:0}
  .brand{position:absolute;left:16px;top:16px;display:flex;align-items:flex-start;gap:16px}
  .brand-mark{width:91px;height:91px;background:var(--navy);border:6px solid #fff}
  .brand-name{font-family:"Cinzel",serif;font-weight:600;font-size:39px;line-height:40px;color:var(--navy);margin-top:4px}
  .feature-icon{position:absolute;left:35px;width:124px;height:124px;border-radius:50%;background:#fff;border:4px solid var(--teal);display:flex;align-items:center;justify-content:center}
  .feature-icon svg{width:76px;height:76px}
  .feature-text{position:absolute;left:184px;width:815px;color:var(--paper-text);font-size:18px;line-height:22.6px;letter-spacing:1.5px;hyphens:auto;-webkit-hyphens:auto}
  .feature-text.loose{font-size:17.5px;line-height:26px;letter-spacing:1.1px}
  .keyword{color:var(--navy)}
  .footer-mark{position:absolute;left:710px;top:1252px;width:86px;height:86px;border:5px solid var(--pale);opacity:.8}
  .phone{position:absolute;left:822px;top:1272px;display:flex;align-items:center;gap:6px;font-size:24px;color:var(--navy)}
  .phone svg{width:24px;height:30px}
</style>
</head>
<body>
<div class="flyer-frame">
<div class="flyer">
  <svg class="backdrop" viewBox="0 0 1048 1356" preserveAspectRatio="none" aria-hidden="true">
    <path d="M0 210 C 300 90, 700 20, 1048 40 L1048 1140 C 700 1230, 350 1300, 0 1300 Z" fill="var(--green)"/>
    <path d="M540 82 C 700 40, 900 30, 1048 70 L1048 98 C 900 50, 720 60, 540 82 Z" fill="var(--navy)"/>
    <path d="M0 1256 C 150 1268, 350 1276, 512 1268 C 350 1300, 150 1300, 0 1290 Z" fill="var(--navy)"/>
  </svg>

  <header class="brand">
    <div class="brand-mark"></div>
    <div class="brand-name">Copper Vale<br>Systems</div>
  </header>

  <div class="feature-icon" style="top:206px"><svg viewBox="0 0 76 76"><path d="M6 24h26v-10l18 18-18 18V38H6z" fill="var(--navy)"/><path d="M70 44H48v-10L30 50l18 16V56h22z" fill="var(--navy)"/></svg></div>
  <p class="feature-text" style="top:207px">It's time for a revolution in an industry that depends on effective marketing, tracking marketing campaign effectiveness, and converting interest into procedures. Finally comes the solution: the Copper Vale Clinic Workflow Hub which includes <span class="keyword">connectivity</span> between your marketing records and your patient records. Two databases, one for patients and one for prospective patients, with a single program connecting them. It's simple, it's HIPAA-compliant, and it's only the beginning.</p>

  <div class="feature-icon" style="top:392px"><svg viewBox="0 0 76 76" fill="none" stroke="var(--navy)" stroke-width="2.5"><ellipse cx="38" cy="40" rx="8" ry="12"/><ellipse cx="38" cy="40" rx="14" ry="20"/><ellipse cx="38" cy="40" rx="20" ry="28"/><ellipse cx="38" cy="40" rx="26" ry="34"/></svg></div>
  <p class="feature-text" style="top:391px">Contact with prospective and current patients is key in a market of elective procedures. Communication must be efficient, standardized, but also <span class="keyword">personalized</span>. The Copper Vale Clinic Workflow Hub does it all by incorporating the patient and contact database information in your communications. The Hub offers an array of customizable, personalized emails, texts, and even printouts for appointment reminders, surgery preparation information, and referral programs - all with a few clicks.</p>

  <div class="feature-icon" style="top:579px"><svg viewBox="0 0 76 76" fill="var(--navy)"><rect x="8" y="8" width="28" height="28"/><rect x="40" y="8" width="28" height="28"/><rect x="8" y="40" width="28" height="28"/><rect x="40" y="40" width="28" height="28"/></svg></div>
  <p class="feature-text" style="top:581px">With your key devices linked together in an integrated system, the Copper Vale Clinic Workflow Hub offers significant <span class="keyword">protection</span> for you and your practice. In addition to streamlining operations, not having to enter data multiple times means you are protected from<br>human errors that can lead to lawsuits.</p>

  <div class="feature-icon" style="top:765px"><svg viewBox="0 0 76 76"><path d="M4 36 C 10 14, 66 14, 72 36 Z" fill="var(--navy)"/><path d="M38 36v26c0 6-8 6-8 0" fill="none" stroke="var(--navy)" stroke-width="3"/></svg></div>
  <p class="feature-text" style="top:773px">In the digital age our industry still requires patients to fill out forms with pen and paper which in turn have to be entered into a database by hand. Technicians must take digital information from [device], print it out into physical paper, then enter the data back into digital format. We say, "No more." With the Copper Vale Clinic Workflow Hub your practice will enjoy full digital <span class="keyword">integration</span> of all key equipment, including the laser, the Wavefront, and the HIPAA-compliant databases that connect them.</p>

  <div class="feature-icon" style="top:952px"><svg viewBox="0 0 76 76"><circle cx="38" cy="42" r="28" fill="var(--navy)"/><circle cx="38" cy="42" r="22" fill="#fff"/><rect x="33" y="6" width="10" height="8" fill="var(--navy)"/><path d="M38 24l5 18-5 18-5-18z" fill="var(--navy)"/></svg></div>
  <p class="feature-text loose" style="top:963px">Lorem ipsum dolor sit amet, consectetuer adipiscing elit, sed diam nonummy nibh euismod tincidunt ut laoreet dolore magna aliquam erat volutpat. Ut wisi enim ad minim veniam, quis nostrud exerci tation ullamcorper suscipit lobortis nisl ut aliquip ex ea commodo consequat. Duis autem vel eum iriure dolor in hendrerit in vulputate velit esse <span class="keyword">time</span> consequat, vel illum dolore eu feugiat nulla.</p>

  <div class="feature-icon" style="top:1130px"><svg viewBox="0 0 76 76" fill="var(--navy)"><rect x="6" y="58" width="7" height="10"/><rect x="16" y="54" width="7" height="14"/><rect x="26" y="48" width="7" height="20"/><rect x="36" y="40" width="7" height="28"/><rect x="46" y="32" width="7" height="36"/><rect x="56" y="24" width="7" height="44"/><path d="M6 52 C 30 48, 48 34, 58 16 L52 14 L68 4 L68 22 L63 18 C 52 38, 32 52, 6 56z"/></svg></div>
  <p class="feature-text loose" style="top:1127px">Lorem ipsum dolor sit amet, consectetuer adipiscing elit, sed diam nonummy nibh euismod tincidunt ut laoreet dolore magna aliquam erat volutpat. Ut wisi enim ad minim veniam, quis nostrud exerci tation ullamcorper <span class="keyword">rise</span> lobortis nisl ut<br>aliquip ex ea commodo consequat. Duis autem vel eum iriure<br>dolor in hendrerit in vulputate.</p>

  <div class="footer-mark"></div>
  <div class="phone">
    <svg viewBox="0 0 24 30"><path d="M6 2l5 1 1 7-4 2c1 5 3 8 7 10l3-3 6 3-1 5c-2 2-5 2-8 1C8 24 3 16 2 8 2 5 3 3 6 2z" fill="var(--teal)"/></svg>
    <span>555-014-2270</span>
  </div>
</div>
</div>
</body>
</html>
```